Harborlight Capital Estates business card

We are a real estate advisory and investment company. We are specialized in assisting high networth individuals to invest in real estate overseas. We deliver a very personalized service, anticipating all the potential challenges an investor can face, and making it easy and safe for them. We also co-invest with our clients, assuring them that each project will be looked after as it is our own, and at the same time giving them the extra booth on confidence to invest.

We need a business card design. The business card must have a very premium, high-end look, reflecting principles like "commitment", "trust" and "timeless (but contemporary)". We look for long term relationships with our clients, and we grow with their referrals. We are all about conquering the confidence of the clients by always delivering above the expectations performance.

Target Market(s)

High net worth individuals.

Industry/Entity Type

Real Estate

Contact Information for Business Card

Please consider places on the business card for:

Name
Function (bellow name in smaller size text)

Mobile phone
E-mail
Call ID
Chat ID

Adress (3 lines)

Also include the following locations references:
PORTUGAL * DUBAI * HONG KONG

Website: www.hcestates-example.com

Requirements
Must have
• Company Logo

```html
<!DOCTYPE html>
<html lang="en">
<head>
<meta charset="utf-8">
<title>Harborlight Capital Estates – Business Card</title>
<link rel="stylesheet" href="https://fonts.googleapis.com/css2?family=Noto+Serif:wght@400;700&display=swap">
<style>
  :root {
    --backdrop: #7c7978;
    --card-white: #ffffff;
    --brand-blue: #2ea9e0;
    --rule-grey: #6d6e71;
    --text-white: #ffffff;
  }
  * { box-sizing: border-box; margin: 0; padding: 0; }
  html, body {
    width: 1200px; height: 852px; overflow: hidden;
    background: var(--backdrop);
    font-family: "Noto Serif", Georgia, serif;
  }
  .stage { position: relative; width: 1200px; height: 852px; }
  .card {
    position: absolute;
    width: 448px; height: 273px;
    border-radius: 14px;
    background: var(--card-white);
    overflow: hidden;
  }
  .card--front { left: 374px; top: 123px; }
  .card--back  { left: 375px; top: 457px; }

  .wave { position: absolute; inset: 0; width: 448px; height: 273px; }

  .front-brand {
    position: absolute; left: 24px; top: 40px; width: 130px;
    color: var(--brand-blue);
    font-weight: 700; font-size: 13px; line-height: 1.2;
    letter-spacing: 0.3px;
  }

  .contact {
    position: absolute; right: 22px; top: 62px; width: 260px;
    text-align: right; color: var(--text-white);
  }
  .contact__name { font-weight: 700; font-size: 15px; letter-spacing: 1px; line-height: 20px; padding-right: 21px; }
  .contact__title { font-size: 9.5px; letter-spacing: 0.6px; line-height: 14px; padding-right: 21px; }
  .contact__list { list-style: none; margin-top: 16px; }
  .contact__row {
    display: flex; justify-content: flex-end; align-items: center; gap: 7px;
    font-size: 12px; letter-spacing: 0.8px; height: 19.5px;
  }
  .contact__address { font-size: 12px; letter-spacing: 0.8px; line-height: 14.5px; margin: 2px 0 6px; padding-right: 21px; }
  .icon { width: 14px; height: 14px; flex: none; }

  .back-brand {
    position: absolute; left: 0; right: 0; top: 110px;
    text-align: center; color: var(--brand-blue);
    font-weight: 700; font-size: 23px; letter-spacing: 1.5px;
  }
  .back-brand__rule {
    position: absolute; left: 102px; width: 244px; top: 150px;
    border-top: 1.5px solid var(--rule-grey);
  }
  .locations {
    position: absolute; left: 0; right: 0; top: 203px;
    text-align: center; color: var(--brand-blue);
    font-size: 13px; letter-spacing: 2.4px;
  }
  .locations__sep { color: var(--rule-grey); margin: 0 4px; }
</style>
</head>
<body>
<main class="stage">
  <section class="card card--front" aria-label="Business card front">
    <svg class="wave" viewBox="0 0 448 273" aria-hidden="true">
      <path d="M0,124 C110,136 190,110 260,76 C330,42 400,24 448,18 L448,273 L0,273 Z" fill="#2ea9e0"/>
      <path d="M0,117 C110,129 190,103 260,69 C330,35 400,17 448,11" fill="none" stroke="#2ea9e0" stroke-width="1.2"/>
    </svg>

    <div class="front-brand">Harborlight<br>Capital Estates</div>

    <div class="contact">
      <p class="contact__name">Name Here</p>
      <p class="contact__title">Function Title</p>
      <ul class="contact__list">
        <li class="contact__row">Mobile phone
          <svg class="icon" viewBox="0 0 14 14"><rect x="4" y="1" width="7" height="12" rx="1.3" fill="none" stroke="#fff" stroke-width="1.1"/><circle cx="7.5" cy="11" r="0.7" fill="#fff"/></svg></li>
        <li class="contact__row">E-mail
          <svg class="icon" viewBox="0 0 14 14"><rect x="0.5" y="3" width="13" height="9" fill="#fff"/><path d="M0.5,3 L7,8 L13.5,3" fill="none" stroke="#2ea9e0" stroke-width="1"/></svg></li>
        <li class="contact__row">Call ID
          <svg class="icon" viewBox="0 0 14 14"><circle cx="7" cy="7" r="6" fill="#fff"/></svg></li>
        <li class="contact__row">Chat ID
          <svg class="icon" viewBox="0 0 14 14"><circle cx="7" cy="7" r="6" fill="#fff"/></svg></li>
      </ul>
      <p class="contact__address">Address line 1<br>Address lines 2<br>Address lines 3</p>
      <p class="contact__row">www.hcestates-example.com
        <svg class="icon" viewBox="0 0 14 14" fill="none" stroke="#fff" stroke-width="1"><circle cx="7" cy="7" r="6"/><ellipse cx="7" cy="7" rx="2.6" ry="6"/><path d="M1,7 H13 M2,4 H12 M2,10 H12"/></svg></p>
    </div>
  </section>

  <section class="card card--back" aria-label="Business card back">
    <div class="back-brand">Harborlight Capital Estates</div>
    <div class="back-brand__rule"></div>
    <p class="locations">Portugal<span class="locations__sep">|</span>Dubai<span class="locations__sep">|</span>Hong Kong</p>
  </section>
</main>
</body>
</html>
```